Information One Page for Email

I am looking for a informative attachment I can send with an introductive email for Ridgeview Cable Works. Something I can also Mail.

Ridgeview Cable Works is the leader in Rebar Post Tension Cable Placement and Post Tension Cable repair. Outside of cable placement and repair we do concrete repair, Parking Garage restoration and

Content

Post Tension Repair and Concrete Restoration
Post-tensioning is a revolutionary method in concrete construction that enhances the strength and durability of structures. However, like all construction ele-ments, post-tension cables can experience wear and damage over time. Ensuring timely and effective repair is crucial for maintaining the safety and integrity of your building.
Why Post-Tension Cable Repair is Essential
1. **Structural Integrity**: Damaged or deteriorated cables can compromise the structural integrity of your building, leading to safety hazards and potential structural failures.
2. **Extended Lifespan**: Regular maintenance and repair of post-tension cables extend the lifespan of your structure, ensuring it remains safe and function-al for years to come.
3. **Cost-Effective**: Addressing cable issues early on prevents more severe damage and costly repairs down the line.
Common Signs of Post-Tension Cable Issues
- Cracks in concrete surfaces
- Unusual noises or popping sounds
- Visible cable ends or broken strands
- Water leakage through cracks
Our Repair Process
1. **Inspection and Assessment**: Our team conducts a thorough inspection to identify the extent of the damage and determine the appropriate repair meth-ods.
2. **Cable Repair or Replacement**: Depending on the severity, we either re-pair the existing cables or replace them with new ones to restore full functional-ity.
3. **Sealing and Protection**: After repairing, we seal the affected areas to protect against moisture and future damage.
4. **Quality Assurance**: We perform rigorous quality checks to ensure the repairs meet industry standards and the structure is safe for use.
Why Choose Us
- **Expertise and Experience**: With years of experience in post-tension cable repair, our team is skilled in handling even the most complex repairs efficiently and effectively.
- **Advanced Technology**: We use the latest technology and materials to ensure durable and long-lasting repairs.
- **Customer Satisfaction**: Our commitment to quality and customer satisfaction sets us apart. We work closely with our clients to ensure their needs are met and expectations exceeded.
Contact Us
If you suspect issues with your post-tension cables or need a routine inspection, don't hesitate to contact us. Our experts are ready to provide the best solutions to keep your structures safe and secure.
Ensure the safety and longevity of your building with our professional post-tension cable repair services. Trust us to deliver quality and reliability every time.

```html
<!DOCTYPE html>
<html lang="en">
<head>
<meta charset="utf-8">
<title>Ridgeview Cable Works – Post Tension Repair Flyer</title>
<link href="https://fonts.googleapis.com/css2?family=Poppins:wght@400;600;700&display=swap" rel="stylesheet">
<style>
:root{
  --green:#117136;
  --green-soft:rgba(17,113,54,.55);
  --charcoal:#4a4a4a;
  --ink:#2b2b2b;
  --paper:#ffffff;
  --stage:#eaeaec;
}
*{margin:0;padding:0;box-sizing:border-box}
html,body{width:1200px;height:1200px;overflow:hidden}
body{background:var(--stage);font-family:'Poppins',sans-serif;color:var(--ink);position:relative}
.page{position:absolute;width:534px;background:var(--paper);overflow:hidden}
.page--front{left:47px;top:47px;height:762px}
.page--back{left:623px;top:389px;height:754px}
.abs{position:absolute}
.brand{display:flex;align-items:center;gap:7px;color:var(--green);font-weight:600;font-size:15px;line-height:1.1}
.brand-mark{width:12px;height:12px;background:var(--green);flex:none}
.photos{position:absolute;left:0;top:0}
.title{left:227px;top:22px;color:var(--green);font-weight:700;font-size:20px;line-height:23px}
.call{left:227px;top:78px;font-weight:700;font-size:20px;color:var(--charcoal)}
.intro{left:227px;top:115px;width:307px;height:82px;background:var(--green);color:#fff;
  font-size:9.1px;line-height:10.8px;padding:8px 16px 0 22px;
  clip-path:polygon(0 0,279px 0,307px 25px,307px 100%,0 100%)}
.section-title{color:var(--green);font-weight:700;font-size:15px;line-height:16.5px}
.reason-icon{position:absolute;top:456px;width:48px;height:48px;border-radius:50%;background:var(--charcoal)}
.reason{position:absolute;top:512px;width:144px}
.reason h3,.step h3{color:var(--green);font-weight:700;font-size:10.8px;margin-bottom:8px;white-space:nowrap}
.reason p,.step p{font-size:9.2px;line-height:10.8px;color:var(--ink)}
.signs{left:0;top:622px;width:534px;height:102px;background:var(--charcoal);color:#fff}
.signs h2{position:absolute;left:37px;top:8px;font-size:13.5px;font-weight:600}
.sign{position:absolute;top:41px;width:120px}
.sign-flag{width:25px;height:21px;background:var(--green);border-radius:2px;color:#fff;font-weight:700;font-size:14px;text-align:center;line-height:21px;margin-left:1px}
.sign p{font-size:9.2px;line-height:10.8px;margin-top:9px}
.url{left:36px;top:322px;color:var(--green);font-weight:700;font-size:13.5px}
.process{left:0;top:359px;width:534px;height:189px;background:var(--green);color:#fff}
.process h2{position:absolute;left:36px;top:6px;font-size:13.5px;font-weight:600}
.step{position:absolute;width:182px}
.process .step h3,.process .step p{color:#fff}
.step--wide-title h3{font-size:10px}
.step-icon{position:absolute;width:26px;height:26px}
.choose-title{left:36px;top:560px;color:var(--green);font-weight:700;font-size:13.5px}
.perk{position:absolute;left:72px;width:234px;font-size:9.2px;line-height:10.8px}
.perk b{color:var(--green);font-weight:700}
.perk-tick{position:absolute;left:36px;width:16px;height:16px}
.contact{left:329px;top:548px;width:152px;height:206px;background:var(--charcoal);color:#fff;padding:16px 8px 0 8px;overflow:hidden}
.contact h2{font-size:17px;font-weight:700;line-height:20px}
.contact .phone{font-size:12px;font-weight:700;margin-top:8px;white-space:nowrap}
.contact .web{font-size:7.6px;font-weight:700;margin-top:1px;white-space:nowrap}
.contact p{font-size:6.7px;line-height:8.6px;margin-top:9px}
</style>
</head>
<body>

<section class="page page--front">
  <svg class="photos" width="534" height="762" viewBox="0 0 534 762" role="img" aria-label="Photographs of a rebar and post-tension cable grid and a parking structure under construction">
    <defs>
      <linearGradient id="fieldTone" x1="0" y1="0" x2="0" y2="1">
        <stop offset="0" stop-color="#8c9a7a"/><stop offset=".4" stop-color="#6e6a5c"/><stop offset="1" stop-color="#7b6f5e"/>
      </linearGradient>
      <linearGradient id="siteTone" x1="0" y1="0" x2="0" y2="1">
        <stop offset="0" stop-color="#c9ccd0"/><stop offset=".5" stop-color="#8e9196"/><stop offset=".75" stop-color="#5d6a55"/><stop offset="1" stop-color="#a69c8c"/>
      </linearGradient>
    </defs>
    <polygon points="144,96 0,338 0,410 142,335 338,438 332,196" fill="url(#fieldTone)"/>
    <polygon points="257,276 332,196 534,197 534,314 338,438 189,382" fill="url(#siteTone)"/>
    <polygon points="144,96 0,395 338,438" fill="var(--green-soft)"/>
    <polygon points="257,276 189,382 338,438" fill="var(--green-soft)"/>
    <polygon points="0,410 142,335 338,438 0,438" fill="#fff"/>
  </svg>

  <div class="abs brand" style="left:37px;top:38px"><span class="brand-mark"></span><span>Ridgeview<br>Cable Works</span></div>
  <h1 class="abs title">Post Tension Repair and<br>Concrete Restoration</h1>
  <div class="abs call">Call !(555) 014-2870</div>
  <p class="abs intro">Post-tensioning is a revolutionary method in concrete construction that enhances the strength and durability of structures. However, like all construction ele-ments, post-tension cables can experience wear and damage over time. Ensuring timely and effective repair is crucial for maintaining the safety and integrity of your building.</p>

  <h2 class="abs section-title" style="left:37px;top:412px">Why Post-Tension Cable Repair<br>is Essential</h2>

  <div class="reason-icon" style="left:35px">
    <svg width="48" height="48" viewBox="0 0 48 48" fill="none" stroke="#fff" stroke-width="1.4"><rect x="13" y="15" width="22" height="18"/><path d="M13 21h22M13 27h22M19 15v18M25 15v18M31 15v18M19 15l6 6M25 15l-6 6"/></svg>
  </div>
  <div class="reason-icon" style="left:203px">
    <svg width="48" height="48" viewBox="0 0 48 48" fill="none" stroke="#fff" stroke-width="1.6"><path d="M16 13h16M16 35h16M18 13c0 8 12 8 12 11s-12 3-12 11M30 13c0 8-12 8-12 11s12 3 12 11"/><path d="M20 33l4-4 4 4z" fill="#fff"/></svg>
  </div>
  <div class="reason-icon" style="left:376px">
    <svg width="48" height="48" viewBox="0 0 48 48" fill="none" stroke="#fff" stroke-width="1.4"><circle cx="25" cy="20" r="7"/><path d="M25 16v8M23 18h3a1.5 1.5 0 010 3h-2a1.5 1.5 0 000 3h3M25 8v3M21 9l1 2M29 9l-1 2M11 31h6l6 2h8l6-4M11 36h8l10 1 10-6"/></svg>
  </div>

  <div class="reason" style="left:37px"><h3>1. **Structural Integrity**:</h3><p>Damaged or deteriorated cables can compromise the structural integrity of your building, leading to safety hazards and potential strtuctural failures.</p></div>
  <div class="reason" style="left:206px"><h3>2. **Extended Lifespan**:</h3><p>Regular maintenance and repair of post-tension cables extend the lifespan of your structure, ensuring it remains safe and function-al for years to come.</p></div>
  <div class="reason" style="left:377px;width:146px"><h3>3. **Cost-Effective**:</h3><p>Addressing cable issues early on prevents more severe damage and costly repairs down the line.<br>Common Signs of Post-Tension Cable Issues</p></div>

  <div class="abs signs">
    <h2>Common Signs of Post-Tension Cable Issues</h2>
    <div class="sign" style="left:38px"><div class="sign-flag">!</div><p>Cracks in concrete<br>surfaces</p></div>
    <div class="sign" style="left:173px"><div class="sign-flag">!</div><p>Unusual noises or<br>popping sounds</p></div>
    <div class="sign" style="left:292px"><div class="sign-flag">!</div><p>Visible cable ends<br>or broken strands</p></div>
    <div class="sign" style="left:416px"><div class="sign-flag">!</div><p>Water leakage<br>through cracks</p></div>
  </div>
</section>

<section class="page page--back">
  <svg class="photos" width="534" height="754" viewBox="0 0 534 754" role="img" aria-label="Photographs of a worker breaking out damaged concrete and a restored parking garage deck">
    <defs>
      <linearGradient id="workTone" x1="0" y1="0" x2="1" y2="1">
        <stop offset="0" stop-color="#7d7f74"/><stop offset=".5" stop-color="#9a9889"/><stop offset="1" stop-color="#5f6358"/>
      </linearGradient>
      <linearGradient id="deckTone" x1="0" y1="0" x2="0" y2="1">
        <stop offset="0" stop-color="#c5c7c6"/><stop offset=".45" stop-color="#9fa3a4"/><stop offset="1" stop-color="#8c8f8c"/>
      </linearGradient>
    </defs>
    <polygon points="145,0 364,68 190,266 143,238 0,316 0,248" fill="url(#workTone)"/>
    <polygon points="364,68 534,105 534,226 338,343 190,266" fill="url(#deckTone)"/>
    <polygon points="145,0 15,300 338,343" fill="var(--green-soft)"/>
    <polygon points="300,190 190,266 338,343" fill="var(--green-soft)"/>
    <polygon points="0,316 143,238 338,343 0,343" fill="#fff"/>
  </svg>

  <div class="abs brand" style="left:383px;top:26px"><span class="brand-mark"></span><span>Ridgeview<br>Cable Works</span></div>
  <div class="abs url">www.ridgeviewcableworks.com</div>

  <div class="abs process">
    <h2>Our Repair Process</h2>
    <svg class="step-icon" style="left:35px;top:40px" viewBox="0 0 26 26" fill="none" stroke="#fff" stroke-width="1.5"><circle cx="10" cy="10" r="8"/><path d="M6 10l3 3 5-6M16 16l8 8"/></svg>
    <div class="step" style="left:72px;top:40px"><h3>1. **Inspection and Assessment**:</h3><p>Our team conducts a thorough inspection to identify the extent of the damage and determine the appropriate repair meth-ods.</p></div>
    <svg class="step-icon" style="left:297px;top:38px;width:34px" viewBox="0 0 34 26" fill="none" stroke="#fff" stroke-width="1.3"><path d="M2 16c10-2 18-3 24-8 3-3 4-5 4-6M2 19c10-1 20-2 26-10M2 22l10-4M6 14l6 3"/></svg>
    <div class="step step--wide-title" style="left:337px;top:40px;width:168px"><h3>2. **Cable Repair or Replacement**:</h3><p>Depending on the severity, we either re-pair the existing cables or replace them with new ones to restore full functional-ity.</p></div>
    <svg class="step-icon" style="left:36px;top:117px" viewBox="0 0 26 26" fill="none" stroke="#fff" stroke-width="1.6"><path d="M13 2l10 4v7c0 6-4 10-10 12C7 23 3 19 3 13V6z"/><rect x="10" y="12" width="6" height="5" fill="#fff"/><path d="M11 12v-2a2 2 0 014 0v2"/></svg>
    <div class="step" style="left:72px;top:117px"><h3>3. **Sealing and Protection**:</h3><p>After repairing, we seal the affected areas to protect against moisture and future damage</p></div>
    <svg class="step-icon" style="left:298px;top:118px" viewBox="0 0 26 26" fill="none" stroke="#fff" stroke-width="1.8"><circle cx="12" cy="14" r="10"/><path d="M7 13l5 5L24 3"/></svg>
    <div class="step" style="left:337px;top:117px;width:174px"><h3>4. **Quality Assurance**:</h3><p>We perform rigorous quality checks to ensure the repairs meet industry standards and the structure is safe for use.</p></div>
  </div>

  <h2 class="abs choose-title">Why Choose Us</h2>
  <svg class="perk-tick" style="top:601px" viewBox="0 0 16 16" fill="none" stroke="var(--green)" stroke-width="1.4"><circle cx="8" cy="8" r="7"/><path d="M4.5 8l2.5 2.5L13 3"/></svg>
  <p class="perk" style="top:595px"><b>- **Expertise and Experience**:</b> With years of experience in post-tension cable repair, our team is skilled in handling even the most complex repairs efficiently and effectively.</p>
  <svg class="perk-tick" style="top:654px" viewBox="0 0 16 16" fill="none" stroke="var(--green)" stroke-width="1.4"><circle cx="8" cy="8" r="7"/><path d="M4.5 8l2.5 2.5L13 3"/></svg>
  <p class="perk" style="top:650px"><b>- **Advanced Technology**:</b> We use the latest technology and materials to ensure durable and long-lasting repairs.</p>
  <svg class="perk-tick" style="top:702px" viewBox="0 0 16 16" fill="none" stroke="var(--green)" stroke-width="1.4"><circle cx="8" cy="8" r="7"/><path d="M4.5 8l2.5 2.5L13 3"/></svg>
  <p class="perk" style="top:694px"><b>- **Customer Satisfaction**:</b> Our commitment to quality and customer satisfaction sets us apart. We work closely with our clients to ensure their needs are met and expectations exceeded.</p>

  <div class="abs contact">
    <h2>Contact Us!</h2>
    <div class="phone">Call !(555) 014-2870</div>
    <div class="web">www.ridgeviewcableworks.com</div>
    <p>If you suspect issues with your post-tension cables or need a routine inspection, don't hesitate to contact us. Our experts are ready to provide the best solutions to keep your structures safe and secure.</p>
    <p>Ensure the safety and longevity of your building with our professional post-tension cable repair services. Trust us to deliver quality and reliability every time.</p>
  </div>
</section>

</body>
</html>
```